K&T Holdings

Design a modern simple business card. I have attached a clean version of a card we like form Marrowfield Partners another company we own. I also attached the old K&T card design and logo and a couple of ideas we had but just can't finalize on whether we like them or not. We would like to include the 20 year logo somewhere on the card.

```html
<!DOCTYPE html>
<html lang="en">
<head>
<meta charset="utf-8">
<title>K&amp;T Holdings – Business Card</title>
<link rel="stylesheet" href="https://fonts.googleapis.com/css2?family=Montserrat:wght@400;500;600;700;800&display=swap">
<style>
  :root {
    --navy: #2b2a6b;
    --navy-light: #34337a;
    --grey: #8a8a8c;
    --white: #ffffff;
    --page: #ececed;
    --text-soft: #e4e4f0;
  }
  * { margin: 0; padding: 0; box-sizing: border-box; }
  html, body { width: 1200px; height: 800px; overflow: hidden; }
  body {
    background: var(--page);
    font-family: "Montserrat", sans-serif;
    position: relative;
  }
  .card {
    position: absolute;
    top: 165px;
    width: 276px;
    height: 465px;
    background: var(--navy);
    overflow: hidden;
    color: var(--white);
  }
  .card--front { left: 298px; border-radius: 0 18px 18px 18px; }
  .card--back  { left: 626px; border-radius: 18px 0 0 0; }

  .front-shape { position: absolute; inset: 0; width: 100%; height: 100%; }

  .wordmark {
    position: absolute;
    left: 0; right: 0;
    text-align: center;
    font-weight: 800;
    letter-spacing: 1px;
  }
  .card--front .wordmark { top: 82px; font-size: 50px; color: var(--navy); }
  .card--back .wordmark  { top: 210px; font-size: 62px; color: var(--white); }

  .contact { position: absolute; left: 46px; top: 262px; }
  .contact__name { font-size: 16.5px; font-weight: 700; letter-spacing: 0.6px; line-height: 20px; }
  .contact__title { font-size: 12.5px; font-weight: 400; color: var(--text-soft); line-height: 16px; }
  .contact__list { list-style: none; margin-top: 16px; }
  .contact__item {
    display: flex; align-items: center; gap: 8px;
    font-size: 12.5px; line-height: 19px; color: var(--text-soft);
  }
  .contact__item svg { width: 10px; height: 10px; fill: var(--text-soft); flex: none; }
  .contact__address { font-size: 12.5px; line-height: 15px; color: var(--text-soft); margin-top: 5px; font-style: normal; }

  .wave-band {
    position: absolute; left: 0; right: 0; bottom: 0; height: 38px;
    background: linear-gradient(180deg, var(--navy) 0%, var(--navy-light) 100%);
  }

  .anniversary { position: absolute; top: 42px; left: 0; right: 0; text-align: center; }
  .anniversary__count { font-size: 44px; font-weight: 700; line-height: 44px; letter-spacing: -1px; }
  .anniversary__count span { font-size: 10px; font-weight: 600; letter-spacing: 1px; vertical-align: 22px; margin-left: 2px; }
  .anniversary__range { font-size: 13px; font-weight: 600; letter-spacing: 1px; margin-top: 2px; }

  .tagline {
    position: absolute; top: 362px; left: 0; right: 0;
    display: flex; align-items: center; gap: 6px;
    font-size: 11px; font-weight: 700; letter-spacing: 0.5px; white-space: nowrap;
  }
  .tagline::before, .tagline::after { content: ""; height: 1.5px; background: var(--white); flex: 1; }

  .services {
    position: absolute; top: 386px; left: 0; right: 0; list-style: none;
    text-align: center; font-size: 11px; line-height: 13.5px; color: var(--text-soft);
  }
</style>
</head>
<body>
  <section class="card card--front" aria-label="Business card front">
    <svg class="front-shape" viewBox="0 0 276 465" aria-hidden="true">
      <path d="M0 0 H276 V176 Q138 274 0 176 Z" fill="var(--grey)"/>
      <path d="M0 0 H276 V168 Q138 258 0 168 Z" fill="var(--white)"/>
    </svg>
    <div class="wordmark">K&amp;T</div>
    <div class="contact">
      <h1 class="contact__name">DANIEL WHITFORD</h1>
      <p class="contact__title">IT Director</p>
      <ul class="contact__list">
        <li class="contact__item">
          <svg viewBox="0 0 24 24"><path d="M6.6 10.8a15.2 15.2 0 0 0 6.6 6.6l2.2-2.2c.3-.3.7-.4 1-.2 1.1.4 2.3.6 3.6.6.6 0 1 .4 1 1V20c0 .6-.4 1-1 1A17 17 0 0 1 3 4c0-.6.4-1 1-1h3.5c.6 0 1 .4 1 1 0 1.3.2 2.5.6 3.6.1.3 0 .7-.2 1z"/></svg>
          555-210-4837
        </li>
        <li class="contact__item">
          <svg viewBox="0 0 24 24"><path d="M7 1h10a2 2 0 0 1 2 2v18a2 2 0 0 1-2 2H7a2 2 0 0 1-2-2V3a2 2 0 0 1 2-2zm0 3v14h10V4zm5 15.5a1 1 0 1 0 0 2 1 1 0 0 0 0-2z"/></svg>
          555-318-2046
        </li>
        <li class="contact__item">
          <svg viewBox="0 0 24 24"><path d="M2 4h20v16H2zm2 2v.5l8 5 8-5V6zm0 3v9h16V9l-8 5z"/></svg>
          dwhitford@ktholdings.com
        </li>
      </ul>
      <address class="contact__address">418 Cedar Avenue, Suite 204<br>Millbrook, TX 77412</address>
    </div>
    <div class="wave-band" role="img" aria-label="Decorative wavy line pattern"></div>
  </section>

  <section class="card card--back" aria-label="Business card back">
    <div class="anniversary">
      <p class="anniversary__count">20<span>YEARS</span></p>
      <p class="anniversary__range">2004-2024</p>
    </div>
    <div class="wordmark">K&amp;T</div>
    <p class="tagline">INTERGRATED INDUSTRIAL SERVICES</p>
    <ul class="services">
      <li>Mechanical | Civil</li>
      <li>I&amp;E | Fabrication</li>
      <li>Rotating | Heat Transfer Equipment</li>
    </ul>
  </section>
</body>
</html>
```